Harbourline Conveyancing

We are a legal service provider.
We deal predominately with Real Estate title transfers.
We will be printing on white paper with black ink, so colour is not really needed for the letter head.

I have enclosed our logo which i will like to be incorporated into the letterhead.

I have also attached a copy of our current old letterhead with all our office details on there. Everything that is listed in the current letterhead i would like to be included in the new one.

Target Market(s)

Real Estate, Home buyers & Sellers, Solicitors and Lawyers, Pest & Building Inspectors

Industry/Entity Type

Legal

Font styles to use
Serif

Requirements
Must have
• Simple and Legal looking.

```html
<!DOCTYPE html>
<html lang="en">
<head>
<meta charset="utf-8">
<title>Harbourline Conveyancing — Letterhead</title>
<link rel="stylesheet" href="https://fonts.googleapis.com/css2?family=Libre+Baskerville:wght@400;700&display=swap">
<style>
  :root {
    --ink: #1c1c1c;
    --ink-soft: #3a3a3a;
    --rule: #8f8f8f;
    --paper: #ffffff;
    --page-bg: #ffffff;
  }
  * { margin: 0; padding: 0; box-sizing: border-box; }
  html, body {
    width: 849px; height: 1200px; overflow: hidden;
    background: var(--page-bg);
  }
  .letterhead {
    position: relative;
    width: 849px; height: 1200px;
    background: var(--paper);
    color: var(--ink);
    font-family: "Libre Baskerville", Georgia, serif;
  }
  .brand {
    position: absolute; left: 82px; top: 96px;
    display: flex; align-items: center; gap: 12px;
  }
  .brand-mark {
    width: 22px; height: 22px; background: var(--ink);
  }
  .brand-name {
    font-weight: 700; font-size: 22px; letter-spacing: 1px;
    line-height: 1.1; color: var(--ink);
  }
  .brand-name span { display: block; font-size: 12px; letter-spacing: 2.2px; }
  .licence {
    position: absolute; left: 390px; top: 92px;
  }
  .licence-title {
    font-weight: 700; font-size: 17px; letter-spacing: 0.6px;
    margin-bottom: 9px;
  }
  .licence-line {
    font-weight: 700; font-size: 11.5px; color: var(--ink-soft);
    line-height: 20px;
  }
  .rule {
    position: absolute; left: 48px; right: 48px;
    height: 0; border-top: 1.5px solid var(--rule);
  }
  .rule-top { top: 172px; }
  .rule-bottom { top: 1016px; }
  .footer-centre {
    position: absolute; left: 0; right: 0; top: 1034px;
    text-align: center; font-size: 11px; line-height: 18px;
    color: var(--ink-soft);
  }
  .contacts {
    position: absolute; top: 1106px; font-size: 11px;
    line-height: 16px; color: var(--ink-soft);
  }
  .contacts-phone { left: 85px; }
  .contacts-post { left: 524px; }
  .contacts dt { display: inline-block; width: 70px; }
  .contacts dd { display: inline; }
  .contacts div { white-space: nowrap; }
</style>
</head>
<body>
  <main class="letterhead">
    <header>
      <div class="brand">
        <div class="brand-mark" aria-hidden="true"></div>
        <div class="brand-name">HARBOURLINE<span>CONVEYANCING</span></div>
      </div>
      <div class="licence">
        <p class="licence-title">CERTIFIED PRACTISING CONVEYANCERS</p>
        <p class="licence-line">Licensee: Elena Maris Dorsey</p>
        <p class="licence-line">Certified Practising Conveyancer: 204857</p>
      </div>
    </header>
    <div class="rule rule-top"></div>

    <footer>
      <div class="rule rule-bottom"></div>
      <div class="footer-centre">
        <p>Member of the National Guild of Conveyancers</p>
        <p>A.B.N. 47 302 915 118</p>
        <p>Shop 4, 12-16 Wattle Parade, (Cnr Elm Street) ASHBURY NSW 2193</p>
      </div>
      <dl class="contacts contacts-phone">
        <div><dt>Phone:</dt><dd>02 9061 4420</dd></div>
        <div><dt>Fax:</dt><dd>02 9061 4431</dd></div>
        <div><dt>Mobile:</dt><dd>0412 555 309</dd></div>
      </dl>
      <div class="contacts contacts-post">
        <p>All Correspondence to:</p>
        <p>P.O. Box 7712 Riverwood NSW 2210</p>
        <p>Email: elena.dorsey@harbourline.example</p>
      </div>
    </footer>
  </main>
</body>
</html>
```